Web Design Project

We are a SaaS company that specializes in the thrift industry POS and inventory software. We want a clean and professional site that does NOT look like a template site.

*** A little more about our business -
We offer a SaaS (Software As A Service) for a Point Of Sale and inventory control product specifically for the Thrift / Second hand industry. The software allows them to process inventory, grade/rate it, create the barcoded tags. It the does the whole retail sale process. We also offer tie-ins to Plumora, Zentiq and pebble/vorn mobile apps to support our customers thrift stores.

We need to in incorporate the look/feel and color scheme of our logo.

I would imagine possibly a HTML5 slideshow (3-5 slides) rotating on the home page showing screenshots, etc.

I am envisioning icons representing features of our product.

PLEASE ask questions, I am sure I have left out a ton.

Reason: I am increasing the budget.

Reason: I have had a harder time with content than I thought I would.

Reason: I was very ill, but I am back and want to get it finished up!

Requirements
Must have
• I have attached a couple of our logo's with color options. It needs to flow with that.

I have also attached a screen shot of what I think might work. This DOESN'T suggest that is what I am looking for, just a sample.

I am thinking a home page and maybe one or two sub pages
***Update, I kind of like the following concept for one of the sub-pages
http://www.quelbrix.example/estimate.html

There should also be a place to highlight Plumora and zentiq.

It will be a bilingual / multilingual site, so take that into account
Should not have
• I don't want it to look like a template site. It should be clean and professional.

```html
<!DOCTYPE html>
<html lang="en">
<head>
<meta charset="utf-8">
<title>Resellwise — Track time, monitor expenses and invoice online</title>
<link rel="stylesheet" href="https://fonts.googleapis.com/css2?family=Roboto+Condensed:wght@400;700&family=Arimo:wght@400;700&display=swap">
<style>
:root{
  --header-top:#2f7ea6;
  --header-bottom:#153a52;
  --hero-deep:#0b2a44;
  --hero-bright:#1a8ccc;
  --slate:#2b3b49;
  --slate-light:#3a4b5a;
  --accent:#2aa3e6;
  --page:#f3f4f5;
  --ink:#1d1d1d;
  --body-text:#4a4a4a;
  --footer:#333333;
  --footer-rule:#4a4a4a;
  --footer-text:#d7d7d7;
  --white:#ffffff;
}
*{box-sizing:border-box;margin:0;padding:0}
html,body{width:1117px;height:1200px;overflow:hidden;background:var(--page)}
body{position:relative;font-family:"Arimo",Arial,sans-serif;color:var(--ink)}
.abs{position:absolute}
.cond{font-family:"Roboto Condensed","Arial Narrow",sans-serif}

/* header */
.site-header{left:0;top:0;width:1117px;height:95px;background:linear-gradient(var(--header-top),var(--header-bottom))}
.hatch{left:0;width:1117px;height:6px;background:repeating-linear-gradient(135deg,#111 0 2px,#555 2px 4px)}
.brand{left:142px;top:26px;display:flex;align-items:center;gap:10px}
.brand-mark{width:36px;height:36px;background:var(--accent);border-radius:4px}
.brand-name{font-family:"Roboto Condensed",sans-serif;font-weight:700;font-size:32px;color:#7cc6ef}
.main-nav{top:38px;left:530px;display:flex;gap:22px;align-items:center;font-family:"Roboto Condensed",sans-serif;font-size:18px;color:var(--white)}

/* hero */
.hero{left:0;top:101px;width:1117px;height:316px;background:radial-gradient(ellipse at 72% 40%,var(--hero-bright),var(--hero-deep) 75%)}
.hero-title{left:143px;top:132px;color:var(--white);font-weight:400}
.hero-title span{display:block;white-space:nowrap}
.hero-title .light{font-size:29px;line-height:40px}
.hero-title .strong{font-size:38px;font-weight:700;color:#111;letter-spacing:-.5px;line-height:45px}
.hero-title .strong small{font-size:27px;font-weight:400;color:var(--white);letter-spacing:0}
.hero-title .big{font-size:42px;line-height:48px}
.cta{left:142px;top:341px;width:212px;height:43px;border-radius:4px;background:linear-gradient(#2a86cf,#154f8a);color:var(--white);font-family:"Roboto Condensed",sans-serif;font-size:20px;display:flex;align-items:center;justify-content:space-between;padding:0 16px 0 23px;box-shadow:0 3px 6px rgba(0,0,0,.4)}
.hero-art{left:560px;top:140px;width:455px;height:290px;border-radius:10px;background:linear-gradient(160deg,#e9ecee,#aeb6bc 70%,#c9ced2)}

/* welcome */
.welcome-band{left:0;top:423px;width:1117px;height:127px;background:linear-gradient(var(--slate),var(--slate-light))}
.welcome-title{left:148px;top:428px;font-size:31px;color:var(--white);font-weight:400}
.welcome-text{left:145px;top:468px;width:250px;font-size:11px;line-height:19px;color:var(--white)}
.slider-dots{left:722px;top:445px;display:flex;gap:4px}
.slider-dots span{width:11px;height:11px;border-radius:50%;background:#222}
.slider-dots span:first-child{background:var(--accent)}
.quote{left:500px;top:472px;width:494px;text-align:center;font-size:21px;line-height:26px;color:var(--white)}
.quote em{font-style:normal;color:var(--accent)}

/* tabs */
.tab-band{left:0;top:550px;width:1117px;height:74px;background:linear-gradient(#4a5560,#8b939a 50%,#6f7981)}
.tab{top:558px;height:66px;display:flex;flex-direction:column;align-items:center;justify-content:flex-end;padding-bottom:6px;font-family:"Roboto Condensed",sans-serif;font-size:18px;color:var(--white);gap:4px}
.tab.active{background:linear-gradient(#fff,#eceeef);color:#333;width:98px;left:380px}
.tab svg{width:26px;height:28px}

/* features */
.feature{width:280px}
.feature-icon{position:absolute;left:0;top:0;width:43px;height:43px;border-radius:7px}
.feature h3{position:absolute;left:60px;top:0;font-size:12px;font-weight:700;white-space:nowrap;letter-spacing:.2px}
.feature p{position:absolute;left:60px;top:22px;width:220px;font-size:11px;line-height:19px;color:var(--body-text)}

/* footer */
.site-footer{left:0;top:930px;width:1117px;height:270px;background:var(--footer)}
.footer-heading{font-family:"Roboto Condensed",sans-serif;font-size:19px;color:var(--footer-text);font-weight:400}
.footer-links{list-style:none;font-size:11px;color:var(--footer-text)}
.footer-links li{width:88px;height:30px;line-height:30px;border-bottom:1px solid var(--footer-rule)}
.footer-rule-v{width:1px;height:230px;top:948px;background:var(--footer-rule)}
.recommend{left:423px;top:994px;display:flex;gap:6px;align-items:flex-start;font-size:9px;color:#999}
.recommend-btn{border:1px solid #aaa;background:#eee;color:#333;padding:4px 6px;border-radius:2px}
.social{left:797px;top:972px;width:150px;height:30px;border-radius:15px;background:#d9d9d9;display:flex;align-items:center;justify-content:space-around;padding:0 10px}
.social span{width:19px;height:19px;border-radius:50%;background:#777}
.legal{left:760px;width:226px;text-align:center;font-size:10px;color:var(--white);line-height:17px}
.legal a{color:#c9c9c9;text-decoration:underline}
</style>
</head>
<body>

<header class="abs site-header">
  <div class="abs brand"><span class="brand-mark"></span><span class="brand-name">resellwise</span></div>
  <nav class="abs main-nav">
    <svg width="14" height="13" viewBox="0 0 14 13"><path d="M7 0 14 6H12V13H8.5V9h-3v4H2V6H0Z" fill="#fff"/></svg>
    <span>PRICING &amp; SIGNUP</span><span>SERVICES</span><span>TOUR</span><span>AFFILIATE</span>
  </nav>
</header>
<div class="abs hatch" style="top:95px"></div>

<section class="abs hero"></section>
<div class="abs hatch" style="top:411px"></div>
<div class="abs hero-art" role="img" aria-label="Laptop showing an invoice screen with an alarm clock and floating paper sheets"></div>
<h1 class="abs hero-title cond">
  <span class="light">The Easiest and fastest way to</span>
  <span class="strong">TRACK TIME, MONITOR</span>
  <span class="strong">EXPENSES <small>and</small></span>
  <span class="big">INVOICE ONLINE</span>
</h1>
<a class="abs cta">FIND OUT MORE
  <svg width="18" height="18" viewBox="0 0 18 18"><circle cx="9" cy="9" r="9" fill="#fff"/><path d="M4 9h8M9 5l4 4-4 4" stroke="#1e6fb5" stroke-width="2.2" fill="none"/></svg>
</a>

<section class="abs welcome-band"></section>
<h2 class="abs welcome-title cond">WELCOME</h2>
<p class="abs welcome-text">Lorem ipsum dolor sit amet, consectetuer adipiscing elit, sed diam nonummy nibh euismod tincidunt ut laoreet dolore magna aliquam erat volutpat. Ut wisi enim ad minim veniam</p>
<div class="abs slider-dots"><span></span><span></span><span></span></div>
<p class="abs quote cond">What our users are saying after <em>using easy &amp; secure<br>Invoicing Solution Resellwise</em></p>

<nav class="abs tab-band"></nav>
<div class="abs tab active">
  <svg viewBox="0 0 26 28"><rect x="3" y="4" width="20" height="4" fill="#333"/><rect x="3" y="12" width="14" height="4" fill="#333"/><rect x="3" y="20" width="20" height="4" fill="#333"/></svg>Dashboard</div>
<div class="abs tab" style="left:500px;width:78px">
  <svg viewBox="0 0 26 28"><rect x="3" y="1" width="20" height="26" fill="#f2f2f2" stroke="#999"/><path d="M7 8h12M7 13h12M7 18h12M11 6v16M15 6v16" stroke="#aaa"/></svg>Invoices</div>
<div class="abs tab" style="left:600px;width:86px">
  <svg viewBox="0 0 26 28"><rect x="4" y="3" width="18" height="24" fill="#f7f7f7" stroke="#999"/><path d="M8 10h10M8 15h10M8 20h10" stroke="#999"/><path d="M7 3v-2M11 3v-2M15 3v-2M19 3v-2" stroke="#555" stroke-width="2"/></svg>Estimates</div>
<div class="abs tab" style="left:712px;width:106px">
  <svg viewBox="0 0 26 28"><circle cx="13" cy="15" r="11" fill="#fff" stroke="#666" stroke-width="2"/><path d="M13 8v7l5 3" stroke="#333" stroke-width="2" fill="none"/></svg>Time Tracking</div>
<div class="abs tab" style="left:848px;width:82px">
  <svg viewBox="0 0 26 28"><rect x="2" y="9" width="22" height="12" rx="2" fill="#8c8c8c" transform="rotate(-15 13 15)"/><circle cx="11" cy="14" r="4" fill="#eee"/><circle cx="17" cy="17" r="4" fill="#ddd"/></svg>Expenses</div>

<main>
  <article class="abs feature" style="left:146px;top:662px">
    <div class="feature-icon" style="background:#3a3a3a;border:2px solid #ccc"></div>
    <h3>CONNECTION</h3>
    <p>Lorem ipsum dolor sit amet, consectetuer adipiscing elit, sed diam nonummy nibh euismod tincidunt ut laoreet dolore magna aliquam erat volutpat. Ut wisi enim ad minim veniam.</p>
  </article>
  <article class="abs feature" style="left:439px;top:662px">
    <div class="feature-icon" style="background:#ef6a22"><svg viewBox="0 0 43 43" width="43" height="43"><path d="M21.5 32 10 20a6 6 0 0 1 11.5-6 6 6 0 0 1 11.5 6Z" fill="#fff"/></svg></div>
    <h3>PERSONAL SUPPORT</h3>
    <p>Lorem ipsum dolor sit amet, consectetuer adipiscing elit, sed diam nonummy nibh euismod tincidunt ut laoreet dolore magna aliquam erat volutpat. Ut wisi enim ad minim veniam.</p>
  </article>
  <article class="abs feature" style="left:731px;top:662px">
    <div class="feature-icon" style="background:#5b7394"><svg viewBox="0 0 43 43" width="43" height="43"><circle cx="20" cy="21" r="8" fill="#c9d3df"/></svg></div>
    <h3>SECURITY &amp; RELIABILITY</h3>
    <p>Lorem ipsum dolor sit amet, consectetuer adipiscing elit, sed diam nonummy nibh euismod tincidunt ut laoreet dolore magna aliquam erat volutpat. Ut wisi enim ad minim veniam.</p>
  </article>
  <article class="abs feature" style="left:146px;top:798px">
    <div class="feature-icon" style="background:#e9e9e9;border:1px solid #aaa"><svg viewBox="0 0 43 43" width="43" height="43"><circle cx="21.5" cy="19" r="11" fill="#c8141c"/><path d="M21.5 13v12M15.5 19h12" stroke="#fff" stroke-width="4"/></svg></div>
    <h3>DATA BACKUP &amp; REDUNDANCY</h3>
    <p>Lorem ipsum dolor sit amet, consectetuer adipiscing elit, sed diam nonummy nibh euismod tincidunt ut laoreet dolore magna aliquam erat volutpat. Ut wisi enim ad minim veniam.</p>
  </article>
  <article class="abs feature" style="left:439px;top:798px">
    <div class="feature-icon" style="background:#2c7cc9"></div>
    <h3>UNLIMITED ESSENTIALS</h3>
    <p>Lorem ipsum dolor sit amet, consectetuer adipiscing elit, sed diam nonummy nibh euismod tincidunt ut laoreet dolore magna aliquam erat volutpat. Ut wisi enim ad minim veniam.</p>
  </article>
  <article class="abs feature" style="left:731px;top:798px">
    <div class="feature-icon" style="background:#3ca52c"><svg viewBox="0 0 43 43" width="43" height="43"><path d="M21.5 8v16M14 18l7.5 7.5L29 18" stroke="#fff" stroke-width="4" fill="none"/><path d="M11 27v6h21v-6" stroke="#fff" stroke-width="3" fill="none"/></svg></div>
    <h3>MANY EXTRAS</h3>
    <p>Lorem ipsum dolor sit amet, consectetuer adipiscing elit, sed diam nonummy nibh euismod tincidunt ut laoreet dolore magna aliquam erat volutpat. Ut wisi enim ad minim veniam.</p>
  </article>
</main>

<footer class="abs site-footer"></footer>
<h4 class="abs footer-heading" style="left:130px;top:943px">RESELLWISE</h4>
<ul class="abs footer-links" style="left:130px;top:974px">
  <li>Home</li><li>Benefits</li><li>About Us</li><li>Pricing &amp; Sign Up</li><li>Features</li><li>FAQs</li><li style="border:0">Affiliate</li>
</ul>
<ul class="abs footer-links" style="left:273px;top:974px">
  <li>Blog</li><li>API</li><li>Testimonials</li><li>Tour</li><li>Support</li><li>Contact Us</li><li style="border:0">Invite Friends</li>
</ul>
<div class="abs footer-rule-v" style="left:394px"></div>
<div class="abs footer-rule-v" style="left:753px"></div>
<h4 class="abs footer-heading" style="left:423px;top:943px">LATEST TWEETS</h4>
<div class="abs recommend"><span class="recommend-btn">Recommend</span><span>206 people<br>recommend this. Be</span></div>
<h4 class="abs footer-heading" style="left:799px;top:943px">JOIN US AT</h4>
<div class="abs social">
  <svg width="20" height="20" viewBox="0 0 20 20" role="img" aria-label="RSS feed"><circle cx="4" cy="16" r="2.5" fill="#777"/><path d="M2 9a9 9 0 0 1 9 9M2 3a15 15 0 0 1 15 15" stroke="#777" stroke-width="2.5" fill="none"/></svg>
  <span role="img" aria-label="Streamvale"></span><span role="img" aria-label="Plumora"></span><span role="img" aria-label="Zentiq"></span>
</div>
<p class="abs legal" style="top:1015px">Copyright 2012 Resellwise.<br>All Rights reserved.</p>
<p class="abs legal" style="top:1063px"><a>Privacy Policy</a> &nbsp;|&nbsp; <a>Terms Of Service</a></p>
<p class="abs legal" style="top:1092px;left:740px"><a>Data Backup</a> &nbsp;|&nbsp; <a>Partnership</a></p>
<p class="abs legal" style="top:1120px"><a style="font-weight:700">Feedback</a></p>

</body>
</html>
```